Menu sign design for Italian Deli

Need designs for 2 hanging signs - one sided, full color, full bleed.
One sign finishes at 48" wide by 36" high, the other sign finishes at 24" wide by 36" high. (Copy and Specs included in PDF).

All files to be completed in PDF format, CMYK

Fonts, layout, colors, backgrounds, photos are totally up to you. Once we see some concepts we can give you more direction/ideas.
These signs will be used in an Italian Deli....(maybe pick-up the Italian colors?????)

```html
<!DOCTYPE html>
<html lang="en">
<head>
<meta charset="utf-8">
<title>Deli Menu Sign</title>
<link href="https://fonts.googleapis.com/css2?family=Arimo:wght@400;700&display=swap" rel="stylesheet">
<style>
  :root {
    --frame: #5b4638;
    --cream: #fcf1e6;
    --band: #c8a293;
    --ink: #1c1714;
    --salad: #7fae4a;
    --hotdog: #c98a4a;
    --fish: #d99a3c;
    --fries: #e6c46a;
  }
  * { margin: 0; padding: 0; box-sizing: border-box; }
  html, body { width: 802px; height: 1200px; overflow: hidden; background: var(--frame); }
  .sign {
    position: relative; width: 802px; height: 1200px;
    background: var(--frame); border-radius: 18px;
    font-family: "Arimo", Arial, sans-serif; color: var(--ink);
  }
  .panel { position: absolute; left: 21px; width: 760px; background: var(--cream); }
  .panel--top { top: 13px; height: 415px; border-radius: 14px 14px 0 0; }
  .panel--fish { top: 663px; height: 273px; }
  .band { position: absolute; left: 21px; width: 760px; background: var(--band); }
  .band--one { top: 428px; height: 235px; }
  .band--two { top: 936px; height: 246px; border-radius: 0 0 14px 14px; }
  .photo { position: absolute; width: 353px; border-radius: 14px; }
  .photo--salad { left: 0; top: 16px; height: 210px; background: radial-gradient(circle at 50% 45%, var(--salad), #4f7a2c 55%, #f4f1ea 80%); }
  .photo--hotdog { left: 406px; top: 16px; height: 210px; background: linear-gradient(135deg, #f2efe9 0%, var(--hotdog) 45%, #a04b2a 70%, #e8a14a 100%); }
  .photo--fish { left: 0; top: 12px; height: 228px; background: linear-gradient(160deg, var(--fish), #b96d24 60%, #f0d25a); }
  .photo--fries { left: 406px; top: 12px; height: 228px; background: linear-gradient(200deg, #4aa0d8 0%, var(--fries) 35%, #d3963a 75%); }
  h2 { font-size: 23px; font-weight: 700; text-align: center; letter-spacing: 0.3px; line-height: 28px; }
  .heading { position: absolute; left: 0; width: 760px; }
  .prices { position: absolute; left: 32px; top: 68px; font-size: 21px; border-collapse: collapse; }
  .prices th, .prices td { height: 35px; padding: 0; text-align: center; width: 160px; }
  .prices th { font-weight: 700; }
  .prices th:first-child, .prices td:first-child { width: 273px; text-align: left; }
  .desc { position: absolute; left: 30px; width: 490px; font-size: 21px; line-height: 35px; }
  .price { position: absolute; left: 590px; font-size: 21px; line-height: 35px; }
  .note { font-size: 21px; line-height: 35px; text-align: center; }
</style>
</head>
<body>
<div class="sign">
  <section class="panel panel--top">
    <h2 class="heading" style="top:19px">FRESH GARDEN SALADS:</h2>
    <table class="prices">
      <tr><th></th><th>Small</th><th>Large</th></tr>
      <tr><td>Plain:</td><td>$2.99</td><td>$4.99</td></tr>
      <tr><td>Specialty:</td><td>$4.99</td><td>$7.99</td></tr>
    </table>
    <h2 class="heading" style="top:208px">ROSETTI'S GARBAGE PLATTER:</h2>
    <p class="desc" style="top:265px">Your choice of 2 Hamburgs, Cheeseburgs, Hot Dogs, or Italian Sausages. With Fries and Mac or Potato Salad. Top with Onions, Meat Hot Sauce, Ketchup, or Mustard.</p>
    <p class="price" style="top:352px">$9.99</p>
  </section>
  <div class="band band--one">
    <div class="photo photo--salad" role="img" aria-label="Fresh garden salad in a glass bowl"></div>
    <div class="photo photo--hotdog" role="img" aria-label="Hot dog platter with chips and mac and cheese"></div>
  </div>
  <section class="panel panel--fish">
    <h2 class="heading" style="top:52px">HADDOCK FISH FRY:</h2>
    <p class="heading note" style="top:80px">(Fridays only)</p>
    <p class="desc" style="top:136px">Your choice of Beer Battered, Breaded, or Broiled with Potato Wedges, Coleslaw, Lemon, Salt, Pepper, Butter, Ketchup, and a roll.</p>
    <p class="price" style="top:192px">$9.99</p>
  </section>
  <div class="band band--two">
    <div class="photo photo--fish" role="img" aria-label="Fried haddock fillets with lemon slices"></div>
    <div class="photo photo--fries" role="img" aria-label="Fish and fries with dipping sauce"></div>
  </div>
</div>
</body>
</html>
```